QZmortgage303.com needs a website.

I'm looking for a website that offeres education and courses about the QZ home loan. This will teach people what they need to know about using the QZ loan. I need a website design that will allow the use of video, have sections to educate about the myths out there, use blue and red which are patriotic colors.

```html
<!DOCTYPE html>
<html lang="en">
<head>
<meta charset="utf-8">
<title>QZmortgage303.com – QZ Home Loan Education</title>
<link href="https://fonts.googleapis.com/css2?family=Poppins:wght@400;500;600;700&family=Montserrat:wght@600;700;800&family=Rubik:wght@600;700&display=swap" rel="stylesheet">
<style>
:root{
  --navy:#2b2c6f;
  --navy-dark:#1b1a3a;
  --red:#d4202f;
  --mid:#7a2a5a;
  --text:#3b3b55;
  --grad:linear-gradient(120deg,var(--navy) 0%,var(--mid) 50%,var(--red) 100%);
}
*{box-sizing:border-box;margin:0;padding:0}
html,body{width:1200px;height:4695px;overflow:hidden}
body{position:relative;background:#fff;font-family:"Poppins",sans-serif;color:var(--text)}
.abs{position:absolute}
.btn{position:absolute;display:flex;align-items:center;justify-content:center;color:#fff;background:var(--grad);border-radius:10px;font-size:10px}
.btn.lg{border-radius:16px;font-size:16px}
.para{position:absolute;font-size:13px;line-height:21px;color:var(--text)}
.red-title{position:absolute;color:var(--red);font-family:"Montserrat",sans-serif;font-weight:800;letter-spacing:5px}
.chunky{position:absolute;color:var(--red);font-family:"Rubik",sans-serif;font-weight:700;letter-spacing:2px}
.lead{position:absolute;color:#222;letter-spacing:1px}
.photo{position:absolute}

/* nav */
.hero-shape{position:absolute;left:0;top:0}
.nav-box{position:absolute;left:250px;top:58px;width:595px;height:50px;background:#fff}
.nav a{position:absolute;top:73px;font-size:15px;color:var(--navy);text-decoration:none}
.nav .home{left:270px;top:72px;width:64px;height:20px;background:var(--red);color:#fff;text-align:center;font-size:14px;line-height:20px;clip-path:polygon(0 0,88% 0,100% 100%,0 100%)}

/* login card */
.login{position:absolute;left:622px;top:153px;width:303px;height:268px;background:linear-gradient(135deg,#3a3a86 0%,#7a2c63 55%,#c3253a 100%);border-radius:3px;text-align:center;color:#fff}
.login .small{font-size:14px;letter-spacing:1px;margin-top:2px}
.login .big{font-family:"Montserrat",sans-serif;font-weight:700;font-size:24px;letter-spacing:1px;line-height:26px}
.login .field{position:absolute;left:28px;width:247px;height:24px;background:#fff;border-radius:3px;color:var(--navy);font-size:9px;line-height:24px;letter-spacing:1px}
.login .go{position:absolute;left:117px;top:232px;width:77px;height:20px;background:var(--navy);border-radius:3px;font-size:12px;line-height:20px}

.brand{position:absolute;display:flex;align-items:center;gap:10px;font-family:"Poppins",sans-serif;font-weight:600;font-size:10px;letter-spacing:2px;color:#444}
.brand i{width:26px;height:26px;border:3px solid #444;border-radius:50%;display:block}

/* teachers */
.teacher .pic{position:absolute;width:176px;height:176px;border-radius:50%;background:radial-gradient(circle at 50% 40%,#d9cfc6,#7d776f)}
.teacher .social{position:absolute;width:66px;height:66px;border-radius:50%;background:#2a62b6;border:5px solid #fff;box-shadow:0 0 0 2px var(--red)}
.teacher p{position:absolute;width:200px;text-align:center;font-size:11px;line-height:18px;letter-spacing:.6px;color:#555}

/* lessons */
.lesson .frame{position:absolute;height:133px;padding:3px;background:var(--grad)}
.lesson .frame div{width:100%;height:100%}
.lesson h4{position:absolute;font-size:13px;font-weight:700;color:#222;letter-spacing:1px}
.lesson p{position:absolute;font-size:13px;line-height:18px;letter-spacing:.8px;color:#444}

/* eligibility */
.pill{position:absolute;left:266px;width:617px;height:55px;background:#e6e7ee;border-radius:4px;display:flex;align-items:center}
.pill i{width:17px;height:17px;border-radius:50%;background:var(--navy);margin-left:40px}
.pill span{flex:1;text-align:center;font-family:"Montserrat",sans-serif;font-weight:700;font-size:22px;letter-spacing:4px;color:var(--navy);margin-right:57px}

/* footer */
.footer{position:absolute;left:20px;top:4219px;width:1166px;height:446px;background:var(--navy-dark);color:#fff}
.footer h5{position:absolute;top:62px;font-family:"Montserrat",sans-serif;font-size:17px;letter-spacing:2px;font-weight:700}
.footer .about{position:absolute;left:57px;top:118px;width:270px;font-size:12px;line-height:21px;letter-spacing:.8px;color:#cfd0e0}
.footer .contact{position:absolute;left:433px;display:flex;align-items:center;gap:24px;font-size:14px;font-weight:600;letter-spacing:2px}
.footer .link{position:absolute;left:840px;display:flex;align-items:center;gap:22px;font-size:14px;font-weight:600;letter-spacing:.6px}
.footer .bottom{position:absolute;left:0;top:352px;width:100%;text-align:center;font-size:13px;line-height:22px;letter-spacing:1px;color:#cfd0e0}
</style>
</head>
<body>

<!-- header decoration -->
<svg class="hero-shape" width="1200" height="450" aria-hidden="true">
  <defs><linearGradient id="hg" x1="0" y1="0" x2="1" y2="1"><stop offset="0" stop-color="#2b2c6f"/><stop offset=".55" stop-color="#7a2a5a"/><stop offset="1" stop-color="#d4202f"/></linearGradient></defs>
  <polygon points="588,0 1200,0 1200,440 1095,440" fill="url(#hg)"/>
</svg>
<div class="nav-box"></div>
<nav class="nav">
  <a class="home">Home</a>
  <a style="left:358px">Survices</a>
  <a style="left:463px">Courses</a>
  <a style="left:560px">About us</a>
  <a style="left:673px">Blog</a>
</nav>

<!-- hero -->
<div class="abs" style="left:115px;top:181px;font-size:12px;font-weight:600;letter-spacing:2px;color:#222">GET YOUR</div>
<div class="red-title" style="left:115px;top:198px;font-size:36px">QZ&nbsp; HOME LOAN</div>
<div class="abs" style="left:115px;top:238px;font-size:32px;letter-spacing:4px;color:#222">Now.</div>
<p class="para" style="left:115px;top:305px;width:400px">Lorem ipsum dolor sit amet, consectetuer adipiscing elit, sed diam nonummy nibh euismod tincidunt ut laoreet dolore magna aliquam erat volutpat. Ut wisi enim ad minim</p>
<div class="btn" style="left:173px;top:415px;width:86px;height:28px">About us +</div>
<div class="btn" style="left:288px;top:415px;width:88px;height:28px">Services +</div>

<div class="brand" style="left:151px;top:543px"><i></i>LARVENTO</div>
<div class="brand" style="left:314px;top:543px"><i style="border-radius:0"></i>QUIBREL</div>
<div class="brand" style="left:151px;top:601px"><i style="border-radius:0"></i>NORVESSA</div>
<div class="brand" style="left:322px;top:601px"><i></i>TAMPRIX</div>

<div class="login" role="img" aria-label="Sign-up card over a faint photo of a house">
  <div class="small" style="margin-top:2px">Ready to get your</div>
  <div class="big">PROPERTY</div>
  <div class="small" style="margin-top:0">Now!</div>
  <div class="field" style="top:86px">First Name</div>
  <div class="field" style="top:134px">Last Name</div>
  <div class="field" style="top:186px">E-Mail</div>
  <div class="go">Log in</div>
</div>
<div class="abs" style="left:771px;top:440px;width:16px;height:16px;border-radius:50%;border:2px solid var(--red);background:radial-gradient(var(--red) 45%,#fff 50%)"></div>
<div class="abs" style="left:796px;top:442px;width:12px;height:12px;border-radius:50%;background:var(--navy)"></div>

<div class="abs" style="left:620px;top:473px;font-size:16px;letter-spacing:1px;color:#222">Best Education For</div>
<div class="chunky" style="left:620px;top:492px;font-size:34px">Best Students</div>
<p class="para" style="left:620px;top:543px;width:300px">Lorem ipsum dolor sit amet, consectetuer adipiscing elit, sed diam nonummy nibh euismod tincidunt ut laoreet dolore</p>

<!-- guide -->
<svg class="abs" style="left:0;top:0" width="1200" height="1120" aria-hidden="true">
  <defs><linearGradient id="fg" x1="0" y1="1" x2="1" y2="0"><stop offset="0" stop-color="#2b2c6f"/><stop offset=".5" stop-color="#7a2a5a"/><stop offset="1" stop-color="#d4202f"/></linearGradient></defs>
  <path d="M785,712 Q900,690 1031,693 L1031,1098 L675,1098 L675,1045 L785,1045 Z" fill="url(#fg)"/>
</svg>
<div class="abs" style="left:545px;top:733px;width:404px;height:303px;background:#fff"></div>
<div class="photo" style="left:550px;top:738px;width:394px;height:293px;background:linear-gradient(135deg,#9ec9d8,#e7e1d6 55%,#c9a56b)" role="img" aria-label="Model house beside stacks of coins and a pie chart"></div>
<div class="abs" style="left:626px;top:631px;width:136px;height:136px;border-radius:50%;background:linear-gradient(150deg,#4a2a70,#2b2c6f);color:#fff;text-align:center;font-family:'Montserrat',sans-serif;font-weight:700">
  <div style="margin-top:32px;font-size:18px;letter-spacing:1px">SCIENCE</div>
  <div style="font-size:38px;line-height:40px">2023</div>
</div>

<div class="abs" style="left:140px;top:740px;font-size:23px;color:#222">Your Complete Guide for</div>
<div class="red-title" style="left:122px;top:775px;font-size:38px;letter-spacing:3px">QZ HOME LOAN</div>
<p class="para" style="left:111px;top:838px;width:440px;font-size:12.5px">Lorem ipsum dolor sit amet, consectetuer adipiscing elit, sed<br>diam nonummy nibh euismod tincidunt ut laoreet dolore magna</p>
<div class="abs" style="left:117px;top:916px;width:18px;height:18px;border-radius:50%;background:var(--navy)"></div>
<div class="abs" style="left:173px;top:914px;font-size:14px;font-weight:700;color:#222">What is QZ LOAN?</div>
<p class="para" style="left:173px;top:940px;width:290px;font-size:12.5px;line-height:17px">Lorem ipsum dolor sit amet, consectetuer adipiscing elit, sed diam</p>
<div class="abs" style="left:117px;top:990px;width:18px;height:18px;border-radius:50%;background:var(--navy)"></div>
<div class="abs" style="left:173px;top:988px;font-size:14px;font-weight:700;color:#222">Are you eligibe for QZ LOAN?</div>
<p class="para" style="left:173px;top:1014px;width:290px;font-size:12.5px;line-height:17px">Lorem ipsum dolor sit amet, consectetuer adipiscing elit, sed diam</p>
<div class="btn" style="left:252px;top:1075px;width:117px;height:33px;border-radius:12px">Learn More..</div>

<!-- teachers -->
<div class="lead" style="left:111px;top:1215px;font-size:30px">Our</div>
<div class="red-title" style="left:111px;top:1258px;font-size:50px;letter-spacing:7px">TEACHERS</div>

<div class="teacher">
  <div class="pic" style="left:100px;top:1399px" role="img" aria-label="Portrait of a male teacher"></div>
  <div class="social" style="left:226px;top:1509px"></div>
  <p style="left:88px;top:1584px">Lorem ipsum dolor sit amet, consectetuer adipiscing elit, sed diam nonummy nibh euismod tincidunt ut laoreet</p>
  <div class="btn" style="left:160px;top:1684px;width:118px;height:32px">Read More +</div>

  <div class="pic" style="left:383px;top:1399px" role="img" aria-label="Portrait of a female teacher"></div>
  <div class="social" style="left:499px;top:1509px"></div>
  <p style="left:371px;top:1584px">Lorem ipsum dolor sit amet, consectetuer adipiscing elit, sed diam nonummy nibh euismod tincidunt ut laoreet</p>
  <div class="btn" style="left:414px;top:1684px;width:118px;height:32px">Read More +</div>

  <div class="pic" style="left:629px;top:1399px" role="img" aria-label="Portrait of a teacher holding folders"></div>
  <div class="social" style="left:749px;top:1509px"></div>
  <p style="left:617px;top:1584px">Lorem ipsum dolor sit amet, consectetuer adipiscing elit, sed diam nonummy nibh euismod tincidunt ut laoreet</p>
  <div class="btn" style="left:664px;top:1684px;width:118px;height:32px">Read More +</div>

  <div class="pic" style="left:890px;top:1399px" role="img" aria-label="Portrait of a bearded male teacher"></div>
  <div class="social" style="left:1013px;top:1509px"></div>
  <p style="left:888px;top:1580px">Lorem ipsum dolor sit amet, consectetuer adipiscing elit, sed diam nonummy nibh euismod tincidunt ut laoreet</p>
  <div class="btn" style="left:929px;top:1684px;width:118px;height:32px">Read More +</div>
</div>

<!-- online -->
<div class="lead" style="left:0;width:1168px;text-align:center;top:1850px;font-size:30px">Start Your Class</div>
<div class="red-title" style="left:0;width:1168px;text-align:center;top:1885px;font-size:48px;letter-spacing:12px">ONLINE</div>
<div class="photo" style="left:0;top:2013px;width:1200px;height:451px;background:linear-gradient(100deg,#7c6a5e 0%,#c9b9a8 40%,#e6ded3 60%,#9a8a7a 100%)" role="img" aria-label="Video still of two colleagues giving a high five at an office desk"></div>
<div class="abs" style="left:525px;top:2195px;width:92px;height:92px;border-radius:50%;background:linear-gradient(120deg,#2b2c6f,#d4202f)">
  <svg width="92" height="92" aria-hidden="true"><polygon points="36,26 36,66 68,46" fill="#fff"/></svg>
</div>

<div class="lesson">
  <div class="frame" style="left:71px;top:2548px;width:239px"><div role="img" aria-label="Hands with a calculator and loan papers" style="background:linear-gradient(135deg,#e8e6e4,#b5aba3)"></div></div>
  <h4 style="left:71px;top:2700px">Lorem ipsum dolor sit</h4>
  <p style="left:71px;top:2720px">amet, consectetuer adipi-<br>scing elit, sed diam</p>
  <div class="frame" style="left:343px;top:2548px;width:237px"><div role="img" aria-label="Cash passing between hands over a laptop" style="background:linear-gradient(135deg,#cfd3d6,#8d949b)"></div></div>
  <h4 style="left:343px;top:2700px">Lorem ipsum dolor sit</h4>
  <p style="left:343px;top:2720px">amet, consectetuer adipi-<br>scing elit, sed diam</p>
  <div class="frame" style="left:613px;top:2548px;width:237px"><div role="img" aria-label="Chart of easy steps to a QZ loan" style="background:linear-gradient(135deg,#f4f4f6,#c7cad3)"></div></div>
  <h4 style="left:613px;top:2700px">Lorem ipsum dolor sit</h4>
  <p style="left:613px;top:2720px">amet, consectetuer adipi-<br>scing elit, sed diam</p>
  <div class="frame" style="left:881px;top:2548px;width:238px"><div role="img" aria-label="House key with a red house keyring on wood" style="background:linear-gradient(135deg,#8a7f74,#5d544c)"></div></div>
  <h4 style="left:884px;top:2702px">Lorem ipsum dolor sit</h4>
  <p style="left:884px;top:2722px">amet, consectetuer adipi-<br>scing elit, sed diam</p>
</div>
<div class="btn lg" style="left:506px;top:2792px;width:191px;height:55px;border-radius:18px;font-size:15px">More leassons+</div>

<!-- gallery -->
<div class="lead" style="left:137px;top:2905px;font-size:30px">Our</div>
<div class="red-title" style="left:137px;top:2943px;font-size:40px;letter-spacing:7px">GALLERY</div>
<div class="photo" style="left:137px;top:3026px;width:292px;height:210px;background:linear-gradient(135deg,#3c3c3c,#8a8077)" role="img" aria-label="Hand placing a wooden block on steps, chalk sketches behind"></div>
<div class="photo" style="left:137px;top:3249px;width:292px;height:213px;background:linear-gradient(135deg,#eeeceb,#a8a09a)" role="img" aria-label="Person working with a calculator and papers"></div>
<div class="photo" style="left:445px;top:3026px;width:287px;height:140px;background:linear-gradient(135deg,#c46a4e,#d9d5d0 60%,#8f9aa6)" role="img" aria-label="Cash handed over a desk with reports"></div>
<div class="photo" style="left:445px;top:3185px;width:287px;height:277px;background:linear-gradient(135deg,#e1e3e5,#8e959b)" role="img" aria-label="Banknotes passed from one hand to another"></div>
<div class="photo" style="left:752px;top:3026px;width:294px;height:210px;background:linear-gradient(135deg,#dfe3e8,#9aa6ad)" role="img" aria-label="Hand holding cash and a phone"></div>
<div class="photo" style="left:750px;top:3249px;width:296px;height:209px;background:linear-gradient(135deg,#3c3c3c,#8a8077)" role="img" aria-label="Hand placing a wooden block on steps, chalk sketches behind"></div>
<div class="btn lg" style="left:493px;top:3528px;width:191px;height:56px;border-radius:18px;font-size:15px;background:linear-gradient(120deg,#2b2c6f 40%,#d4202f)">Lode more +</div>

<!-- eligibility -->
<div class="chunky" style="left:126px;top:3658px;font-size:44px">Check Your Eligibility</div>
<p class="para" style="left:130px;top:3720px;width:460px;font-size:15px;line-height:22px;letter-spacing:.8px">Lorem ipsum dolor sit amet, consectetuer adip-<br>iscing elit, sed diam nonummy nibh euismod</p>
<div class="abs" style="left:131px;top:3811px;width:913px;height:308px;background:linear-gradient(90deg,#2b2c6f 0%,#5b2b66 45%,#b52a3b 80%,#d4202f 100%)" role="img" aria-label="Faint photo of a small house model in hands over a blue to red tint"></div>
<div class="pill" style="top:3887px"><i></i><span>I want to buy a Home</span></div>
<div class="pill" style="top:3991px"><i></i><span>I want refinance a Home</span></div>

<!-- footer -->
<footer class="footer">
  <h5 style="left:57px">About Us</h5>
  <h5 style="left:422px">Get In Touch</h5>
  <h5 style="left:834px">Useful Links</h5>
  <p class="about">Lorem ipsum dolor sit amet, consectetuer adipiscing elit, sed diam nonummy nibh euismod tincidunt ut laoreet dolore magna aliquam erat volutpat. Ut wisi enim ad minim veniam, quis nostrud exerci tation ullamcorper suscipit lobortis nisl ut</p>

  <div class="contact" style="top:126px">
    <svg width="22" height="16" aria-hidden="true"><rect x="1" y="1" width="20" height="14" fill="none" stroke="#fff" stroke-width="2"/><polyline points="1,1 11,9 21,1" fill="none" stroke="#fff" stroke-width="2"/></svg>
    <span>hello@qzmortgage303.com</span></div>
  <div class="contact" style="top:183px">
    <svg width="22" height="22" aria-hidden="true"><path d="M5 2 L9 2 L10 7 L7 9 Q9 14 13 15 L15 12 L20 13 L20 17 Q19 20 16 20 Q4 18 2 6 Q2 3 5 2 Z" fill="#fff"/></svg>
    <span>+1-555-0142-303</span></div>
  <div class="contact" style="top:243px">
    <svg width="22" height="26" aria-hidden="true"><path d="M11 1 Q20 1 20 10 Q20 16 11 25 Q2 16 2 10 Q2 1 11 1 Z" fill="#fff"/><circle cx="11" cy="10" r="3.5" fill="#1b1a3a"/></svg>
    <span>12 Harbor Lane, Westfield</span></div>

  <div class="link" style="top:121px"><svg width="10" height="14" aria-hidden="true"><polygon points="0,0 10,7 0,14" fill="#fff"/></svg>Lorem ipsum dolor</div>
  <div class="link" style="top:155px"><svg width="10" height="14" aria-hidden="true"><polygon points="0,0 10,7 0,14" fill="#fff"/></svg>sit amet cosetetuer</div>
  <div class="link" style="top:190px"><svg width="10" height="14" aria-hidden="true"><polygon points="0,0 10,7 0,14" fill="#fff"/></svg>adipiscing elitsed</div>
  <div class="link" style="top:224px"><svg width="10" height="14" aria-hidden="true"><polygon points="0,0 10,7 0,14" fill="#fff"/></svg>diam nonummy</div>
  <div class="link" style="top:259px"><svg width="10" height="14" aria-hidden="true"><polygon points="0,0 10,7 0,14" fill="#fff"/></svg>nibh eismod tincunt</div>
  <div class="link" style="top:293px"><svg width="10" height="14" aria-hidden="true"><polygon points="0,0 10,7 0,14" fill="#fff"/></svg>laoreet dolore</div>

  <p class="bottom">Lorem ipsum dolor sit amet, consectetuer adipiscing elit, sed diam nonummy nibh euis-<br>mod tincidunt ut laoreet dolore magna aliquam erat volutpat. Ut wisi enim ad minim</p>
</footer>

</body>
</html>
```